Korbin Airworks. "Clean air, every single time"!

Good day< Does your company do face mask? that is question 1. and lets finish the stationary design and I will pay for that now? 2 If your company has BLACK HATS now I would want to do some of those? 3 I notice do you do BANNER'S and or something I can put on van's magnet type or on a building! )k that's enough but for now lets start with the stationary stuff? let me know you should have my information, and the design look's GREAT!!! Thank you..

```html
<!DOCTYPE html>
<html lang="en">
<head>
<meta charset="utf-8">
<title>Korbin Airworks – Letterhead</title>
<link rel="stylesheet" href="https://fonts.googleapis.com/css2?family=Encode+Sans+Condensed:wght@400&family=Lato:wght@400&family=Raleway:wght@400;800&display=swap">
<style>
  :root {
    --backdrop: #d6d6d6;
    --paper: #ffffff;
    --ink: #111111;
    --text: #5a5a5a;
    --text-soft: #666666;
    --band-dark: #231f20;
    --band-grey: #9a9b9f;
  }
  * { margin: 0; padding: 0; box-sizing: border-box; }
  html, body {
    width: 1056px; height: 1200px; overflow: hidden;
    background: var(--backdrop);
  }
  .letterhead {
    position: absolute; left: 104px; top: 0;
    width: 848px; height: 1200px;
    background: var(--paper);
    color: var(--text);
  }
  .brand {
    position: absolute; left: 80px; top: 65px; width: 209px;
    text-align: center; color: var(--ink);
    font-family: "Raleway", sans-serif; font-weight: 800;
  }
  .brand-mark {
    display: block; width: 71px; height: 71px; margin: 0 auto 8px;
    border-radius: 50%; background: var(--ink);
  }
  .brand-name { font-size: 27px; line-height: 29px; letter-spacing: 0.5px; }
  .brand-tagline { font-size: 14px; line-height: 20px; margin-top: 3px; }

  .contact {
    position: absolute; left: 598px; top: 88px;
    font-family: "Lato", sans-serif; font-size: 14.5px; color: var(--text-soft);
    list-style: none;
  }
  .contact .address { line-height: 19px; }
  .contact .address:nth-child(2) { margin-bottom: 8px; }
  .contact .channel { display: flex; align-items: center; height: 22px; }
  .contact svg { width: 13px; height: 13px; margin: 0 15px 0 1px; fill: var(--band-dark); }

  .date, .recipient-name, .recipient-role, .closing { position: absolute; left: 80px; font-family: "Raleway", sans-serif; }
  .date { top: 410px; font-size: 18px; }
  .recipient-name { top: 447px; font-size: 29px; font-weight: 800; letter-spacing: 0.3px; }
  .recipient-role { top: 490px; font-size: 19px; }

  .body-copy {
    position: absolute; left: 80px; top: 562px; width: 689px;
    font-family: "Encode Sans Condensed", sans-serif; font-size: 17px; line-height: 29.5px;
    text-align: justify;
  }
  .body-copy p + p { margin-top: 29.5px; }
  .closing { top: 888px; font-family: "Encode Sans Condensed", sans-serif; font-size: 18.5px; }
  .signature {
    position: absolute; left: 83px; top: 932px; width: 86px; height: 61px;
    background: linear-gradient(135deg, #f2f2f2, #e4e4e4);
  }

  .footer-band { position: absolute; left: 0; top: 1114px; width: 848px; height: 53px; }
  .footer-band .dark { position: absolute; left: 0; top: 0; width: 629px; height: 53px; background: var(--band-dark); }
  .footer-band .grey { position: absolute; right: 0; top: 0; width: 131px; height: 53px; background: var(--band-grey); }
  .footer-band .ring {
    position: absolute; left: 621px; top: -24px; width: 101px; height: 101px;
    border-radius: 50%; background: var(--paper);
  }
  .footer-band .emblem {
    position: absolute; left: 636px; top: -9px; width: 72px; height: 72px;
    border-radius: 50%; background: var(--ink);
  }
</style>
</head>
<body>
<main class="letterhead">
  <header>
    <div class="brand">
      <span class="brand-mark"></span>
      <div class="brand-name">KORBIN<br>AIRWORKS</div>
      <div class="brand-tagline">"Clean air, every single time"</div>
    </div>
    <ul class="contact">
      <li class="address">1234 First Line Address</li>
      <li class="address">5678 Second Line Address</li>
      <li class="channel">
        <svg viewBox="0 0 24 24" aria-hidden="true"><path d="M6.6 10.8a15.1 15.1 0 0 0 6.6 6.6l2.2-2.2c.3-.3.7-.4 1-.2 1.1.4 2.3.6 3.6.6.6 0 1 .4 1 1V20c0 .6-.4 1-1 1A17 17 0 0 1 3 4c0-.6.4-1 1-1h3.5c.6 0 1 .4 1 1 0 1.3.2 2.5.6 3.6.1.3 0 .7-.2 1z"/></svg>
        (777) 888-7777
      </li>
      <li class="channel">
        <svg viewBox="0 0 24 24" aria-hidden="true"><path d="M2 5h20v14H2z M2 5l10 8 10-8" stroke="#fff" stroke-width="1.5"/></svg>
        info@yourmail.com
      </li>
      <li class="channel">
        <svg viewBox="0 0 24 24" aria-hidden="true"><path d="M12 2a10 10 0 1 0 0 20 10 10 0 0 0 0-20zm0 2c.9 0 2.3 2 2.8 5H9.2C9.7 6 11.1 4 12 4zM4.3 11h4.8a17 17 0 0 0 0 2H4.3a8 8 0 0 1 0-2zm.7 4h4.3c.3 1.6.8 3 1.4 4a8 8 0 0 1-5.7-4zm4-6H5a8 8 0 0 1 5.7-4c-.6 1-1.1 2.4-1.4 4zm3 11c-.9 0-2.3-2-2.8-5h5.6c-.5 3-1.9 5-2.8 5zm3.1-7h-6.2a15 15 0 0 1 0-2h6.2a15 15 0 0 1 0 2zm-1.8 6c.6-1 1.1-2.4 1.4-4H19a8 8 0 0 1-5.7 4zm1.6-6a17 17 0 0 0 0-2h4.8a8 8 0 0 1 0 2zm-.2-4c-.3-1.6-.8-3-1.4-4A8 8 0 0 1 19 9z"/></svg>
        www.yourwebsite.com
      </li>
    </ul>
  </header>

  <p class="date">10 December, 2020</p>
  <h1 class="recipient-name">DANIEL HARPER</h1>
  <p class="recipient-role">Cheif Executive Officer</p>

  <section class="body-copy">
    <p>Contrary to popular belief, Lorem Ipsum is not simply random text. It has roots in a piece of classical Latin literature from 45 BC, making it over 2000 years old. Harold Brennick, a Latin professor at Marlowe Ridge College in Virginia, looked up one of the more obscure Latin words, consectetur.</p>
    <p>Lorem Ipsum comes from sections 1.10.32 and 1.10.33 of "de Finibus Bonorum et Malorum" (The Extremes of Good and Evil) by Lucan Ferro, written in 45 BC. This book is a treatise on the theory of ethics, very popular during the Renaissance. The first line of Lorem Ipsum.</p>
    <p>The standard chunk of Lorem Ipsum used since the 1500s is reproduced below for those interested.</p>
  </section>

  <p class="closing">Best Regards</p>
  <div class="signature" role="img" aria-label="Handwritten signature of the sender"></div>

  <footer class="footer-band">
    <span class="dark"></span>
    <span class="grey"></span>
    <span class="ring"></span>
    <span class="emblem"></span>
  </footer>
</main>
</body>
</html>
```